Trading Company needs a business card design, letter head design and email signature

We need a double-sided business card design, letter head design and an email signature. We have a logo design.

Possible Tag Lines:
• “Connecting Worlds, Building Excellence.”
• “Global Sourcing, Local Excellence.”
• “Bridging Borders, Building Quality.”
• “Worldwide Partnerships, Superior Goods.”
• “Where Quality Meets Affordability”

Services Offered:
Procurement
Fabrication
Distribution
Logistics
Import/Export

Requirements
Must have
• Nice quality double sided Business Card design, Letterhead design needs to be A4
Nice to have
• possible ideas on tag lines

```html
<!DOCTYPE html>
<html lang="en">
<head>
<meta charset="utf-8">
<title>Forgeway Stationery</title>
<link href="https://fonts.googleapis.com/css2?family=Montserrat:wght@400;500;600;700;800&family=Lato:wght@400;700&family=Raleway:wght@400&display=swap" rel="stylesheet">
<style>
  :root{
    --red:#e8262a;
    --ink:#3c3d3f;
    --grey:#6d6e70;
    --slate:#5b5e60;
    --light:#8a8c8e;
    --black:#151515;
    --board:#b8bbbf;
    --paper:#ffffff;
  }
  *{box-sizing:border-box;margin:0;padding:0}
  html,body{width:1200px;height:926px;overflow:hidden}
  body{position:relative;background:linear-gradient(180deg,#c0c3c7 0%,#b3b6ba 60%,#aeb1b5 100%);font-family:"Lato",sans-serif;color:var(--grey)}
  .abs{position:absolute}
  .brand-bar{left:0;top:0;width:1200px;height:141px;background:var(--black)}
  .brand{display:flex;flex-direction:column;align-items:center;gap:10px;font-family:"Montserrat",sans-serif;font-weight:800;color:var(--red);letter-spacing:.06em}
  .brand-mark{background:var(--red)}
  .brand-bar .brand{position:absolute;left:0;right:0;top:32px;font-size:24px}
  .brand-bar .brand-mark{width:30px;height:30px}

  .sheet{position:absolute;background:var(--paper);box-shadow:3px 4px 8px rgba(0,0,0,.28);overflow:hidden}
  .accent-bar{position:absolute;left:0;bottom:0;background:var(--red)}
  .corner-block{position:absolute;background:var(--slate)}
  .corner-block::before{content:"";position:absolute;left:-28%;top:18%;width:48%;height:82%;background:var(--red)}

  .person{font-family:"Montserrat",sans-serif;font-weight:500;color:var(--ink);text-transform:uppercase;letter-spacing:.01em}
  .person b{color:var(--red);font-weight:700}
  .role{font-family:"Lato",sans-serif;color:var(--grey)}
  .rule{height:1px;background:var(--light)}
  .contacts{list-style:none;font-family:"Lato",sans-serif;color:var(--grey)}
  .contacts li{display:flex;align-items:flex-start;gap:4px}
  .icon{flex:none;display:block}

  /* business card front */
  .card-front{left:52px;top:370px;width:268px;height:161px}
  .card-front .person{position:absolute;left:19px;top:19px;font-size:11px}
  .card-front .role{position:absolute;left:19px;top:31px;font-size:9px}
  .card-front .rule{position:absolute;left:19px;top:47px;width:30px}
  .card-front .contacts{position:absolute;left:19px;top:83px;font-size:5.6px;line-height:1.25}
  .card-front .contacts li{margin-bottom:4.5px}
  .card-front .icon{width:7px;height:7px}
  .card-front .accent-bar{width:170px;height:4px}
  .card-front .corner-block{left:200px;top:38px;width:68px;height:123px}

  /* business card back */
  .card-back{left:349px;top:371px;width:268px;height:161px;background:var(--black)}
  .card-back .brand{position:absolute;left:0;right:0;top:48px;font-size:17px}
  .card-back .brand-mark{width:22px;height:22px}
  .services{position:absolute;left:0;right:0;top:123px;text-align:center;font-family:"Montserrat",sans-serif;font-weight:600;font-size:6px;color:#fff;line-height:8.4px;letter-spacing:.02em}
  .services span::before{content:"•";color:var(--red);margin:0 3px 0 4px}
  .services .row2{position:relative;display:inline-block;padding:0 2px;background:var(--black)}
  .services-line{position:absolute;left:0;right:0;top:135px;height:.7px;background:var(--red)}

  /* email signature */
  .signature-block{left:52px;top:554px;width:565px;height:143px}
  .signature-block .brand{position:absolute;left:18px;top:40px;width:92px;font-size:15px}
  .signature-block .brand-mark{width:20px;height:20px}
  .signature-block .person{position:absolute;left:121px;top:20px;font-size:10.5px}
  .signature-block .role{position:absolute;left:121px;top:32px;font-size:8.6px}
  .signature-block .rule{position:absolute;left:121px;top:47px;width:28px}
  .signature-block .contacts{position:absolute;left:121px;top:56px;font-size:7px;line-height:1.3}
  .signature-block .contacts li{margin-bottom:5px;gap:4px}
  .signature-block .icon{width:9px;height:9px}
  .signature-block .accent-bar{width:470px;height:4px}
  .signature-block .corner-block{left:498px;top:26px;width:67px;height:117px}

  /* letterhead */
  .letterhead{left:662px;top:192px;width:486px;height:683px}
  .letterhead .brand{position:absolute;left:31px;top:30px;width:112px;font-size:17px}
  .letterhead .brand-mark{width:26px;height:26px}
  .sender{position:absolute;right:30px;top:30px;list-style:none;text-align:right;font-family:"Lato",sans-serif;font-size:7.8px;color:var(--grey);line-height:1.25}
  .sender li{display:flex;justify-content:flex-end;align-items:flex-start;gap:4px;margin-bottom:6px}
  .sender .icon{width:10px;height:10px}
  .recipient{position:absolute;left:31px;top:183px;font-family:"Montserrat",sans-serif}
  .recipient h2{font-size:15px;font-weight:700;color:var(--red);margin-bottom:4px}
  .recipient p{font-size:9px;color:var(--light);line-height:1.2;margin-bottom:4px}
  .date{position:absolute;right:30px;top:255px;font-family:"Montserrat",sans-serif;font-weight:500;font-size:11px;color:var(--grey)}
  .body-copy{position:absolute;left:32px;width:424px;font-family:"Raleway",sans-serif;font-size:11px;line-height:15.3px;color:var(--light);text-align:justify}
  .body-copy.first{top:284px}
  .body-copy.second{top:406px}
  .sign-off{position:absolute;left:32px;top:505px;font-family:"Montserrat",sans-serif;font-weight:600;font-size:11.5px;color:var(--ink)}
  .handwriting{position:absolute;left:56px;top:530px;width:77px;height:47px;background:linear-gradient(135deg,#eeeeee,#dcdcdc);border-radius:4px}
  .letterhead .accent-bar{width:400px;height:3.5px}
  .letterhead .corner-block{left:412px;top:573px;width:74px;height:110px}
</style>
</head>
<body>
<svg width="0" height="0" style="position:absolute" aria-hidden="true">
  <defs>
    <symbol id="i-pin" viewBox="0 0 10 10"><rect width="10" height="10" rx="1.5" fill="#e8262a"/><path d="M5 2a2.2 2.2 0 0 0-2.2 2.2C2.8 6 5 8.3 5 8.3S7.2 6 7.2 4.2A2.2 2.2 0 0 0 5 2zm0 3.1a.9.9 0 1 1 0-1.8.9.9 0 0 1 0 1.8z" fill="#fff"/></symbol>
    <symbol id="i-pin-dark" viewBox="0 0 10 10"><rect width="10" height="10" rx="1.5" fill="#5b5e60"/><path d="M5 2a2.2 2.2 0 0 0-2.2 2.2C2.8 6 5 8.3 5 8.3S7.2 6 7.2 4.2A2.2 2.2 0 0 0 5 2zm0 3.1a.9.9 0 1 1 0-1.8.9.9 0 0 1 0 1.8z" fill="#fff"/></symbol>
    <symbol id="i-phone" viewBox="0 0 10 10"><rect width="10" height="10" rx="1.5" fill="#e8262a"/><path d="M3.1 2.2l1.1 1.4-.6.8c.4.9 1 1.5 1.9 1.9l.8-.6 1.4 1.1-.6 1c-2.6-.2-4.8-2.4-5-5z" fill="#fff"/></symbol>
    <symbol id="i-mail" viewBox="0 0 10 10"><rect width="10" height="10" rx="1.5" fill="#e8262a"/><rect x="2" y="3" width="6" height="4.2" fill="none" stroke="#fff" stroke-width=".8"/><path d="M2 3l3 2.4L8 3" fill="none" stroke="#fff" stroke-width=".8"/></symbol>
    <symbol id="i-web" viewBox="0 0 10 10"><rect width="10" height="10" rx="1.5" fill="#e8262a"/><path d="M3 2l4.5 3.4-2 .3 1.2 2.2-.9.5-1.2-2.2L3 7.4z" fill="#fff"/></symbol>
  </defs>
</svg>

<header class="abs brand-bar">
  <div class="brand"><span class="brand-mark"></span>FORGEWAY</div>
</header>

<section class="sheet card-front" aria-label="Business card front">
  <p class="person">Daniel R. <b>Whitmore</b></p>
  <p class="role">Managing Director</p>
  <div class="rule"></div>
  <ul class="contacts">
    <li><svg class="icon"><use href="#i-pin-dark"/></svg><span>712 Harbor Street<br>Baltimore, MD 21230</span></li>
    <li><svg class="icon"><use href="#i-phone"/></svg><span>+00 555 019 42</span></li>
    <li><svg class="icon"><use href="#i-mail"/></svg><span>hello@forgeway.co</span></li>
    <li><svg class="icon"><use href="#i-web"/></svg><span>www.forgeway.co</span></li>
  </ul>
  <div class="corner-block"></div>
  <div class="accent-bar"></div>
</section>

<section class="sheet card-back" aria-label="Business card back">
  <div class="brand"><span class="brand-mark"></span>FORGEWAY</div>
  <div class="services-line"></div>
  <p class="services">
    <span>PROCUREMENT</span><span>FABRICATION</span><span>DISTRIBUTION</span><br>
    <em class="row2" style="font-style:normal"><span>LOGISTICS</span><span>IMPORT/EXPORT</span></em>
  </p>
</section>

<section class="sheet signature-block" aria-label="Email signature">
  <div class="brand"><span class="brand-mark"></span>FORGEWAY</div>
  <p class="person">Daniel R. <b>Whitmore</b></p>
  <p class="role">Managing Director</p>
  <div class="rule"></div>
  <ul class="contacts">
    <li><svg class="icon"><use href="#i-pin-dark"/></svg><span>712 Harbor Street<br>Baltimore, MD 21230</span></li>
    <li><svg class="icon"><use href="#i-phone"/></svg><span>+00 555 019 42</span></li>
    <li><svg class="icon"><use href="#i-mail"/></svg><span>hello@forgeway.co</span></li>
    <li><svg class="icon"><use href="#i-web"/></svg><span>www.forgeway.co</span></li>
  </ul>
  <div class="corner-block"></div>
  <div class="accent-bar"></div>
</section>

<section class="sheet letterhead" aria-label="Letterhead">
  <div class="brand"><span class="brand-mark"></span>FORGEWAY</div>
  <ul class="sender">
    <li><span>712 Harbor Street<br>Baltimore, MD 21230</span><svg class="icon"><use href="#i-pin"/></svg></li>
    <li><span>+00 555 019 42</span><svg class="icon"><use href="#i-phone"/></svg></li>
    <li><span>hello@forgeway.co</span><svg class="icon"><use href="#i-mail"/></svg></li>
    <li><span>www.forgeway.co</span><svg class="icon"><use href="#i-web"/></svg></li>
  </ul>
  <div class="recipient">
    <h2>Clara Benson</h2>
    <p>0123-555-014</p>
    <p>clara@bensonmail.co</p>
    <p>88 Elm Ridge Rd. Suite<br>4 Austin, TX 0000</p>
  </div>
  <p class="date">12 December, 2024</p>
  <p class="body-copy first">Lorem ipsum dolor sit amet, consectetuer adipiscing elit, sed diam nonummy nibh euismod tincidunt ut laoreet dolore magna aliquam erat volutpat. Ut wisi enim ad minim veniam, quis nostrud exerci tation ullamcorper suscipit lobortis nisl ut aliquip ex ea commodo consequat. Duis autem vel eum iriure dolor in hendrerit in vulputate velit esse molestie consequat, vel illum dolore eu feugiat nulla facilisis at vero eros et accumsan et iusto odio dignissim qui blandit praesent luptatum zzril delenit augue duis dolore te feugait nulla facilisi.</p>
  <p class="body-copy second">Lorem ipsum dolor sit amet, cons ectetuer adipiscing elit, sed diam nonummy nibh euismod tincidunt ut laoreet dolore magna aliquam erat volutpat. Ut wisi enim ad minim veniam, quis nostrud exerci tation ullamcorper suscipit lobortis nisl ut aliquip ex ea commodo consequat.</p>
  <p class="sign-off">Mr. Daniel R. Whitmore</p>
  <div class="handwriting" role="img" aria-label="Handwritten signature of the sender"></div>
  <div class="corner-block"></div>
  <div class="accent-bar"></div>
</section>
</body>
</html>
```